fernbolt website

commerce website to sell cookeries, brackets, mailboxes and to show off homes built. Modern Steel in design see kelvo rides web page to be like: https://www.kelvorides.com/en/ sorry its blue mantis hosting word press divi

must be able to add products to page

Target Market(s)

mainly western states of U.S.

Industry/Entity Type

Building Product

Coding

Coded - Design and coding required

Number of Pages Required

3 page

Font styles to use
Sans Serif

Colors

Designer to choose colors to be used in the design.

Requirements
Must have
• customers to be able to order products from page
• blue mantis hosting word press divi

```html
<!DOCTYPE html>
<html lang="en">
<head>
<meta charset="utf-8">
<title>Fernbolt — Modern Steel Building Products</title>
<link href="https://fonts.googleapis.com/css2?family=Montserrat:wght@400;500;600;700;800&family=Open+Sans:ital,wght@0,400;0,600;1,400&display=swap" rel="stylesheet">
<style>
:root{
  --navy:#4a5e8c;
  --navy-soft:#6676a3;
  --orange:#fd9a0c;
  --ink:#111;
  --grey:#777;
  --light:#f7f7f7;
  --line:#e2e2e2;
  --white:#fff;
}
*{box-sizing:border-box;margin:0;padding:0}
html,body{width:1200px;height:2979px;overflow:hidden;background:var(--white)}
body{position:relative;font-family:"Open Sans",sans-serif;color:var(--ink)}
.abs{position:absolute}
.brand{display:flex;align-items:center;gap:10px;font-family:"Montserrat",sans-serif;font-weight:700;font-size:24px;color:var(--navy);letter-spacing:1px}
.brand-dot{width:22px;height:22px;border-radius:50%;background:var(--navy)}
.site-header{left:0;top:0;width:1200px;height:114px}
.site-header .brand{position:absolute;left:76px;top:40px}
.main-nav{position:absolute;left:479px;top:50px;display:flex;gap:38px;font-size:14px;color:#888;letter-spacing:.3px}
.main-nav .active{color:var(--navy);font-weight:600}
.btn{display:flex;align-items:center;justify-content:center;border-radius:28px;font-family:"Montserrat",sans-serif;font-weight:500;font-size:15px;color:var(--white)}
.btn-login{left:1008px;top:31px;width:114px;height:52px;background:var(--navy);box-shadow:0 3px 0 #34476f}
.btn-orange{background:var(--orange);box-shadow:0 3px 0 #d97f00}
.hero{left:0;top:114px;width:1200px;height:573px;background:linear-gradient(135deg,#8290b6,#6878a4 55%,#7482ab)}
.hero-title{left:0;width:1200px;top:156px;line-height:88px;text-align:center;font-family:"Montserrat",sans-serif;font-weight:800;font-size:72px;color:var(--white);letter-spacing:-1px}
.hero-text{left:0;width:1200px;top:258px;text-align:center;font-size:18px;line-height:27px;color:var(--white)}
.slider-arrow{width:52px;height:52px;border-radius:50%;display:flex;align-items:center;justify-content:center}
.section-title{left:0;width:1200px;text-align:center;font-family:"Montserrat",sans-serif;font-weight:700;font-size:39px;color:var(--ink)}
.product{width:300px;text-align:center}
.product-photo{width:240px;height:240px;margin:0 auto}
.product h3{margin-top:32px;font-family:"Montserrat",sans-serif;font-weight:500;font-size:20px;color:var(--orange)}
.product p{margin-top:10px;font-size:13px;line-height:23px;color:#555}
.product a{display:block;margin-top:12px;font-family:"Montserrat",sans-serif;font-weight:500;font-size:13px;color:var(--ink);text-decoration:none}
.offers{left:0;top:1281px;width:1200px;height:364px;background:linear-gradient(135deg,#5b6c98,#6d7ca7)}
.offers-title{left:79px;top:60px;font-family:"Montserrat",sans-serif;font-weight:700;font-size:40px;line-height:47px;color:var(--white)}
.offers-text{left:79px;top:172px;font-size:17px;line-height:27px;color:var(--white)}
.review{width:312px;height:363px;border:1px solid var(--line);background:var(--light);padding:40px 32px 0}
.review.featured{background:var(--navy);border-color:var(--navy)}
.review p{margin-top:22px;font-style:italic;font-size:16px;line-height:27px;color:#666}
.review.featured p{color:#e6e9f2}
.review .name{margin-top:14px;font-family:"Montserrat",sans-serif;font-size:15px;color:var(--orange)}
.review .role{margin-top:4px;font-size:13px;color:#888}
.review.featured .role{color:#d0d5e4}
.newsletter{left:77px;top:2312px;width:1045px;height:291px;background:linear-gradient(135deg,#6979a6,#5a6b98)}
.newsletter .hero-text{top:112px}
.field{left:190px;top:187px;width:499px;height:52px;border:2px solid var(--orange);border-radius:28px;background:var(--white);padding-left:22px;display:flex;align-items:center;font-size:15px;color:#555}
.footer-col h4{font-family:"Montserrat",sans-serif;font-weight:600;font-size:17px;color:var(--ink)}
.footer-col ul{list-style:none;margin-top:28px}
.footer-col li{font-size:15px;color:#888;height:31px}
.footer-col li::before{content:"-  ";white-space:pre}
.contact-line{font-size:15px;color:#888;line-height:26px}
.contact-strong{font-size:15px;font-weight:600;color:#333;margin-top:8px}
.social{width:42px;height:42px;border-radius:50%}
.copyright{left:0;top:2896px;width:1200px;height:83px;background:var(--orange);display:flex;align-items:center;justify-content:center;font-size:13px;color:var(--white)}
</style>
</head>
<body>

<header class="abs site-header">
  <div class="brand"><span class="brand-dot"></span>FERNBOLT</div>
  <nav class="main-nav">
    <span class="active">HOME</span><span>PRODUCTS</span><span>HOMES BUILT</span><span>ABOUT</span><span>CONTACT</span>
  </nav>
  <div class="abs btn btn-login">LOG IN</div>
</header>

<section class="abs hero" role="img" aria-label="Bright modern living room with sofas and fireplace, blue tinted">
  <h1 class="abs hero-title">FERNBOLT</h1>
  <p class="abs hero-text">Lorem ipsum dolor sit amet, consectetur adipiscing elit, sed do eiusmod<br>tempor incididunt ut labore et dolore magna aliqua.</p>
  <div class="abs btn btn-orange" style="left:522px;top:334px;width:155px;height:52px">LEARN MORE</div>
  <div class="abs slider-arrow" style="left:51px;top:261px;background:rgba(255,255,255,.35)">
    <svg width="14" height="20" viewBox="0 0 14 20"><path d="M10 2 3 10l7 8" fill="none" stroke="#fff" stroke-width="2"/></svg>
  </div>
  <div class="abs slider-arrow" style="left:1095px;top:261px;border:1px solid rgba(255,255,255,.8)">
    <svg width="14" height="20" viewBox="0 0 14 20"><path d="M4 2l7 8-7 8" fill="none" stroke="#fff" stroke-width="2"/></svg>
  </div>
</section>

<h2 class="abs section-title" style="top:748px">OUR PRODUCTS</h2>
<div class="abs product" style="left:83px;top:833px">
  <div class="product-photo" role="img" aria-label="Stone fire pit with flames in a backyard" style="background:linear-gradient(160deg,#6f8a52,#8c7f70 55%,#5a5550)"></div>
  <h3>STEEL COOKERIES</h3>
  <p>Lorem ipsum dolor sit amet, consectetur<br>labore et dolore magna aliqua.</p>
  <a href="#">LEARN MORE</a>
</div>
<div class="abs product" style="left:450px;top:833px">
  <div class="product-photo" role="img" aria-label="Steel post bracket mounted on a wooden fence" style="background:linear-gradient(180deg,#c99a6e,#b47d55 60%,#8a5e3e)"></div>
  <h3>BRACKETS</h3>
  <p>Lorem ipsum dolor sit amet, consectetur<br>labore et dolore magna aliqua.</p>
  <a href="#">LEARN MORE</a>
</div>
<div class="abs product" style="left:816px;top:833px">
  <div class="product-photo" role="img" aria-label="Steel mailbox on a post in a garden" style="background:linear-gradient(160deg,#4f6a3a,#7b9458 50%,#3f5a2e)"></div>
  <h3>MAIL BOXES</h3>
  <p>Lorem ipsum dolor sit amet, consectetur<br>labore et dolore magna aliqua.</p>
  <a href="#">LEARN MORE</a>
</div>

<section class="abs offers">
  <h2 class="abs offers-title">GET SPECIAL<br>OFFERS</h2>
  <p class="abs offers-text">Lorem ipsum dolor sit amet, consectetur adipiscing elit,<br>sed do eiusmod tempor incididunt</p>
  <div class="abs btn btn-orange" style="left:77px;top:250px;width:156px;height:52px">SEE OFFERS</div>
  <div class="abs" role="img" aria-label="Modern white steel-framed house under blue sky with palm trees" style="left:600px;top:0;width:600px;height:364px;background:linear-gradient(180deg,#8fb2de,#c9d6e6 45%,#b9b3a6 75%,#8c8a7e)"></div>
</section>

<h2 class="abs section-title" style="top:1706px">OUR HAPPY CUSTOMERS</h2>
<svg width="0" height="0" style="position:absolute"><defs><symbol id="quote" viewBox="0 0 52 42"><path d="M10 42C3 42 0 36 0 30 0 16 9 4 20 0l2 5C15 9 12 15 12 20c6 0 10 5 10 11s-5 11-12 11Zm28 0c-7 0-10-6-10-12 0-14 9-26 20-30l2 5c-7 4-10 10-10 15 6 0 10 5 10 11s-5 11-12 11Z" fill="#fd9a0c"/></symbol></defs></svg>
<div class="abs review" style="left:77px;top:1792px">
  <svg width="52" height="42"><use href="#quote"/></svg>
  <p>Lorem ipsum dolor si consectetur adipiscing elit, sed do eiutempor incididunt ut labore et dolmagna aliqua enim ad minim veniam, nostrud exercitation ullamco commodo consequat.</p>
  <div class="name">Client Name</div><div class="role">Lorem ipsum</div>
</div>
<div class="abs review featured" style="left:444px;top:1792px">
  <svg width="52" height="42"><use href="#quote"/></svg>
  <p>Lorem ipsum dolor si consectetur adipiscing elit, sed do eiutempor incididunt ut labore et dolmagna aliqua enim ad minim veniam, nostrud exercitation ullamco commodo consequat.</p>
  <div class="name">Client Name</div><div class="role">Lorem ipsum</div>
</div>
<div class="abs review" style="left:810px;top:1792px">
  <svg width="52" height="42"><use href="#quote"/></svg>
  <p>Lorem ipsum dolor si consectetur adipiscing elit, sed do eiutempor incididunt ut labore et dolmagna aliqua enim ad minim veniam, nostrud exercitation ullamco commodo consequat.</p>
  <div class="name">Client Name</div><div class="role">Lorem ipsum</div>
</div>
<div class="abs slider-arrow" style="left:543px;top:2196px;background:#a9a9a9">
  <svg width="14" height="20" viewBox="0 0 14 20"><path d="M10 2 3 10l7 8" fill="none" stroke="#fff" stroke-width="2"/></svg>
</div>
<div class="abs slider-arrow" style="left:605px;top:2196px;background:var(--orange)">
  <svg width="14" height="20" viewBox="0 0 14 20"><path d="M4 2l7 8-7 8" fill="none" stroke="#fff" stroke-width="2"/></svg>
</div>

<section class="abs newsletter" role="img" aria-label="House exterior with trees, blue tinted">
  <h2 class="abs section-title" style="width:1045px;top:50px;color:#fff">SUBCRIBE NEWSLETTER</h2>
  <p class="abs hero-text" style="width:1045px">Lorem ipsum dolor sit amet, consectetur adipiscing elit, sed do eiusmod<br>tempor incididunt ut labore et dolore magna aliqua.</p>
  <div class="abs field">Enter Email Address</div>
  <div class="abs btn btn-orange" style="left:700px;top:187px;width:156px;height:52px">SUBCRIBE</div>
</section>

<footer>
  <div class="abs brand" style="left:77px;top:2692px"><span class="brand-dot"></span>FERNBOLT</div>
  <div class="abs social" style="left:77px;top:2770px;background:#5068b0" aria-label="Social profile"></div>
  <div class="abs social" style="left:124px;top:2770px;background:#2aa3e3" aria-label="Social profile"></div>
  <div class="abs social" style="left:171px;top:2770px;background:#1b84bf" aria-label="Social profile"></div>
  <div class="abs footer-col" style="left:293px;top:2664px"><h4>PRODUCTS</h4><ul><li>Steel Cookeries</li><li>Brackets</li><li>Mail Boxes</li></ul></div>
  <div class="abs footer-col" style="left:506px;top:2664px"><h4>LINKS</h4><ul><li>Products</li><li>Homes Built</li><li>About</li><li>Contact</li></ul></div>
  <div class="abs footer-col" style="left:719px;top:2664px"><h4>COMPANY</h4><ul><li>Testimonials</li><li>Blog</li><li>Privacy Policy</li><li>Terms &amp; Conditions</li></ul></div>
  <div class="abs footer-col" style="left:932px;top:2664px"><h4>GET IN TOUCH</h4>
    <p class="contact-line" style="margin-top:22px">123, Address, State, Street,<br>City Name, Zip Code</p>
    <p class="contact-strong">123.456.7890</p>
    <p class="contact-strong">info@fernbolt.com</p>
  </div>
  <div class="abs copyright">Copyright © FERNBOLT - 2020 . All Right Reserved.</div>
</footer>

</body>
</html>
```